Brightwell Systems - Company Overview Brochure

We would like a single page A4 Brochure to give to new potential customers to provide a quick overview of our company. This will be used in presales meetings.

We have included the content we would like on the brochure under "Brightwell Systems Marketing Brochure.docx".

We have included two other designs "timebundleterms v4.pdf and Brightwell Public Cloud Plans.pdf" which shows similar marketing brochures we have. We would like these designs to have the same Brightwell Blue and "Specialised Technology Consultancy firm" theme.

Target Market(s)

Technology Sector

Industry/Entity Type

Information Technology

Colors
0054AA
0677BA
7BADD7
CADEEF
E8F1F8

Requirements
Must have
• "Innovative Tech Company Theme".

```html
<!DOCTYPE html>
<html lang="en">
<head>
<meta charset="utf-8">
<title>Brightwell Systems – Company Overview</title>
<link href="https://fonts.googleapis.com/css2?family=Montserrat:wght@400;500;600;700;800&display=swap" rel="stylesheet">
<style>
:root{
  --navy:#1b2766;
  --blue:#0054aa;
  --blue-mid:#0677ba;
  --blue-light:#7badd7;
  --blue-pale:#cadeef;
  --blue-mist:#e8f1f8;
  --grey-text:#6f7480;
  --ink:#2b2f3a;
  --stage:#c9c9c9;
  --panel:#f3f4f7;
}
*{margin:0;padding:0;box-sizing:border-box}
html,body{width:1200px;height:2573px;overflow:hidden}
body{background:var(--stage);font-family:'Montserrat',sans-serif;color:var(--ink);position:relative}
.flyer{position:absolute;left:50px;top:508px;width:1100px;height:1556px;background:#fff;overflow:hidden;box-shadow:0 6px 18px rgba(0,0,0,.18)}
.side-band{position:absolute;left:0;top:0;width:62px;height:1420px;background:linear-gradient(180deg,var(--navy),var(--blue));clip-path:polygon(0 0,100% 0,100% 38%,40% 46%,40% 100%,0 100%)}
.brand{position:absolute;left:105px;top:60px;display:flex;align-items:center;gap:16px}
.brand-dot{width:46px;height:46px;border-radius:50%;background:var(--navy)}
.brand-name{font-weight:700;font-size:36px;color:var(--navy);letter-spacing:1px}
.tagline{position:absolute;left:105px;top:220px;font-size:25px;font-weight:700;color:var(--navy)}
.tagline::before{content:"";display:inline-block;width:2px;height:22px;background:var(--navy);margin-right:12px;vertical-align:-2px}
.headline{position:absolute;left:102px;top:262px;font-weight:800;font-size:84px;line-height:90px;color:var(--navy);letter-spacing:1px}
.headline .accent{color:var(--blue-mid)}
.rule{position:absolute;height:2px;background:var(--blue-mid)}
.intro{position:absolute;left:105px;top:485px;width:530px;font-size:19px;line-height:28px;color:var(--grey-text)}
.commit-head{position:absolute;left:730px;top:188px;width:320px;height:44px;background:var(--navy);border-radius:8px 8px 0 0;color:#fff;font-weight:600;font-size:22px;text-align:center;line-height:44px;letter-spacing:.5px}
.commit-body{position:absolute;left:756px;top:250px;width:268px;font-size:13.5px;line-height:17px;color:var(--grey-text);text-align:justify}
.commit-body p{margin-bottom:17px}
.section-title{position:absolute;font-weight:700;font-size:28px;line-height:30px;color:var(--blue-mid)}
.section-title.dark{color:var(--navy)}
.service{position:absolute;width:200px;text-align:center;font-size:16px;line-height:18px;font-weight:500;color:var(--navy)}
.service svg{display:block;margin:0 auto 10px;width:72px;height:72px}
.dash-h,.dash-v{position:absolute;border-color:#c6cbd6;border-style:dashed;border-width:0}
.dash-h{border-top-width:1.5px;height:0}
.dash-v{border-left-width:1.5px;width:0}
.divider{position:absolute;left:560px;top:690px;width:2px;height:340px;background:var(--navy)}
.policy{position:absolute;top:1127px;width:465px;height:175px;background:var(--panel);padding:20px 20px 0 100px}
.policy svg{position:absolute;left:20px;top:28px;width:64px;height:64px}
.policy h3{font-size:20px;font-weight:600;color:var(--blue-mid);margin-bottom:8px}
.policy p{font-size:13px;line-height:15.5px;color:var(--grey-text)}
.terms{position:absolute;left:0;top:1345px;width:1100px;text-align:center;font-size:16.5px;line-height:25px;font-weight:500;color:var(--ink)}
.terms a{color:var(--blue-mid);text-decoration:none}
.footer{position:absolute;left:0;top:1420px;width:1100px;height:136px;background:linear-gradient(90deg,var(--navy),#15307f 60%,var(--navy))}
.contacts{position:absolute;left:50px;top:55px;right:40px;display:flex;justify-content:space-between;color:#fff;font-size:17.5px}
.contacts span{display:flex;align-items:center;gap:12px}
.contacts svg{width:24px;height:24px}
</style>
</head>
<body>
<div class="flyer">
  <div class="side-band" role="img" aria-label="Dark blue side band with circuit-line texture"></div>

  <div class="brand"><span class="brand-dot"></span><span class="brand-name">BRIGHTWELL</span></div>

  <div class="tagline">SPECIALISED CONSULTIN</div>
  <h1 class="headline">DO IT ONCE<br><span class="accent">DO IT RIGHT</span></h1>
  <div class="rule" style="left:105px;top:462px;width:150px"></div>
  <p class="intro">Brightwell Systems is a Technology Consulting Company based in Perth, Western Australia, which offers customers tailored technical solutions for a range of products.</p>

  <div class="commit-head">OUR COMMITMENT</div>
  <div class="commit-body">
    <p>Our commitment to you is to do things right the first time while being fair but cost-effective. If you're looking for the cheapest consultants, Brightwell may not be the right fit for you.</p>
    <p>We are a specialised consultancy firm that offers tailored solutions to government and the enterprise sector with some of Perth's best consultants.</p>
    <p>In areas such as cybersecurity and business continuity, it pays to get it done correctly the first time in alignment with vendor best practices. There are many ways of doing things in the technology field, and only after understanding all methods of achieving an outcome can you recommend the best solution in alignment with best practices.</p>
  </div>

  <h2 class="section-title" style="left:97px;top:650px">IT SERVICES</h2>
  <div class="rule" style="left:97px;top:688px;width:140px;height:1.5px"></div>

  <div class="dash-h" style="left:97px;top:883px;width:420px"></div>
  <div class="dash-v" style="left:304px;top:705px;height:330px"></div>

  <div class="service" style="left:102px;top:725px">
    <svg viewBox="0 0 72 72"><circle cx="36" cy="36" r="34" fill="var(--blue)"/><circle cx="36" cy="36" r="28" fill="var(--blue-mid)"/><g fill="none" stroke="#fff" stroke-width="3"><circle cx="24" cy="28" r="5"/><circle cx="48" cy="28" r="5"/><circle cx="36" cy="48" r="5"/><path d="M29 28h14M27 32l7 12M45 32l-7 12"/></g></svg>
    Project<br>Intergration
  </div>
  <div class="service" style="left:310px;top:725px">
    <svg viewBox="0 0 72 72"><circle cx="36" cy="36" r="34" fill="var(--blue)"/><circle cx="36" cy="36" r="28" fill="var(--blue-mid)"/><path d="M18 36l10-8 8 4 8-4 10 8-12 10-6-4-6 4z" fill="#fff"/></svg>
    Managed<br>Services
  </div>
  <div class="service" style="left:102px;top:895px">
    <svg viewBox="0 0 72 72"><circle cx="36" cy="36" r="34" fill="var(--blue)"/><circle cx="36" cy="36" r="28" fill="var(--blue-mid)"/><rect x="24" y="33" width="24" height="18" rx="2" fill="#fff"/><path d="M29 33v-5a7 7 0 0 1 14 0v5" fill="none" stroke="#fff" stroke-width="3.5"/><circle cx="36" cy="42" r="2.5" fill="var(--blue)"/></svg>
    Enterprise<br>Security
  </div>
  <div class="service" style="left:310px;top:895px">
    <svg viewBox="0 0 72 72"><circle cx="36" cy="36" r="34" fill="var(--blue)"/><circle cx="36" cy="36" r="28" fill="var(--blue-mid)"/><rect x="19" y="24" width="34" height="24" rx="2" fill="none" stroke="#fff" stroke-width="3"/><path d="M30 31l-5 5 5 5M42 31l5 5-5 5M38 30l-4 12" fill="none" stroke="#fff" stroke-width="2.5"/></svg>
    Software<br>Development
  </div>

  <h2 class="section-title dark" style="left:620px;top:650px;font-size:25px;line-height:27px">ELECTRONIC SECURITY &amp;<br>COMMUNICATION</h2>

  <div class="dash-h" style="left:610px;top:883px;width:440px"></div>
  <div class="dash-v" style="left:818px;top:712px;height:320px"></div>

  <div class="service" style="left:612px;top:725px">
    <svg viewBox="0 0 72 72"><circle cx="36" cy="36" r="34" fill="var(--navy)"/><circle cx="36" cy="36" r="28" fill="#fff"/><circle cx="36" cy="36" r="24" fill="var(--navy)"/><rect x="22" y="28" width="24" height="12" rx="2" fill="#fff" transform="rotate(15 34 34)"/><path d="M30 44v6h14" stroke="#fff" stroke-width="3" fill="none"/></svg>
    CCTV
  </div>
  <div class="service" style="left:818px;top:725px">
    <svg viewBox="0 0 72 72"><circle cx="36" cy="36" r="34" fill="var(--navy)"/><circle cx="36" cy="36" r="28" fill="#fff"/><circle cx="36" cy="36" r="24" fill="var(--navy)"/><path d="M36 20l13 5v10c0 9-6 14-13 17-7-3-13-8-13-17V25z" fill="#fff"/><path d="M38 27l-6 10h5l-3 8 7-11h-5z" fill="var(--navy)"/></svg>
    Intergrated<br>Electronic Security
  </div>
  <div class="service" style="left:612px;top:895px">
    <svg viewBox="0 0 72 72"><circle cx="36" cy="36" r="34" fill="var(--navy)"/><circle cx="36" cy="36" r="28" fill="#fff"/><circle cx="36" cy="36" r="24" fill="var(--navy)"/><g stroke="#fff" stroke-width="3.5" stroke-linecap="round"><path d="M28 24v24M36 22v28M44 24v24"/></g></svg>
    Structured Cabling<br>&amp; Fibre Optics
  </div>
  <div class="service" style="left:818px;top:895px">
    <svg viewBox="0 0 72 72"><circle cx="36" cy="36" r="34" fill="var(--navy)"/><circle cx="36" cy="36" r="28" fill="#fff"/><circle cx="36" cy="36" r="24" fill="var(--navy)"/><circle cx="36" cy="36" r="4" fill="#fff"/><g fill="none" stroke="#fff" stroke-width="3"><path d="M29 29a10 10 0 0 0 0 14M43 29a10 10 0 0 1 0 14M24 24a17 17 0 0 0 0 24M48 24a17 17 0 0 1 0 24"/></g></svg>
    Wireless<br>Communications
  </div>

  <div class="divider"></div>

  <h2 class="section-title dark" style="left:97px;top:1068px">OUR POLICY</h2>

  <div class="policy" style="left:97px">
    <svg viewBox="0 0 64 64"><g fill="var(--navy)"><rect x="30" y="10" width="4" height="40"/><rect x="20" y="50" width="24" height="5"/><rect x="10" y="14" width="44" height="3"/><path d="M4 34h20a10 6 0 0 1-20 0zM40 34h20a10 6 0 0 1-20 0z"/></g><path d="M14 17l-8 17M14 17l8 17M50 17l-8 17M50 17l8 17" stroke="var(--navy)" stroke-width="1.5"/></svg>
    <h3>Be Fair</h3>
    <p>At Brightwell we believe that both parties benefit when pricing is fair. If margins are too low, we may sacrifice service quality, and this ultimately harms our brand. If margins are too high, our customers have an incentive to seek alternative providers, and this compromises our growth and damages client relationships.</p>
  </div>
  <div class="policy" style="left:585px">
    <svg viewBox="0 0 64 64"><g fill="var(--navy)"><rect x="8" y="40" width="8" height="16"/><rect x="20" y="32" width="8" height="24"/><rect x="32" y="24" width="8" height="32"/><rect x="44" y="16" width="8" height="40"/></g><path d="M8 30l18-12 10 6 18-16" stroke="var(--blue-mid)" stroke-width="3" fill="none"/><path d="M48 6h8v8" stroke="var(--blue-mid)" stroke-width="3" fill="none"/></svg>
    <h3>Be Cost-Effective</h3>
    <p>At Brightwell we believe that it is possible to deliver both high quality at a fair cost, by providing services that are intelligent and efficient</p>
  </div>

  <p class="terms">All goods and services provided by Brightwell are provided in accordance with our Standard Terms<br>and Conditions available at <a href="#">https://www.brightwellsystems.example/t&amp;c</a></p>

  <div class="footer">
    <div class="contacts">
      <span><svg viewBox="0 0 24 24"><circle cx="12" cy="12" r="12" fill="var(--blue-mid)"/><path d="M8 6l3 3-1.5 2a8 8 0 0 0 3.5 3.5L15 13l3 3-2 2C10 18 6 14 6 8z" fill="#fff"/></svg>0890001234</span>
      <span><svg viewBox="0 0 24 24"><circle cx="12" cy="12" r="12" fill="var(--blue-mid)"/><rect x="6" y="8" width="12" height="8" fill="#fff"/><path d="M6 8l6 5 6-5" stroke="var(--blue-mid)" stroke-width="1.2" fill="none"/></svg>sales@brightwellsystems.example</span>
      <span><svg viewBox="0 0 24 24"><circle cx="12" cy="12" r="12" fill="var(--blue-mid)"/><g fill="none" stroke="#fff" stroke-width="1.4"><circle cx="12" cy="12" r="6"/><ellipse cx="12" cy="12" rx="2.6" ry="6"/><path d="M6 12h12"/></g></svg>www.brightwellsystems.example</span>
    </div>
  </div>
</div>
</body>
</html>
```